design a beautiful, neat and professional looking 10 page templete for an online course

I designed an online course. It about the newborn adoption process. I need you to design the template for it. Just the first 10 pages is enough. I'm thinking a neutral palette with a pop of a minor color to keep it from being boring. The pop of color should not distract the reader. You can design how you want. If you want to add small details or hearts or a shape in background you can. Just dont overdo it. Sparingly is the key. You can make pages a different color. It just needs to look like a neutral color palette with a small pop of color.
Updates

Low design quality

Target Market(s)

people who are adopting a newborn in the USA

Industry/Entity Type

newborn adoption

Font styles to use
Sans Serif

Colors

Designer to choose colors to be used in the design.

Requirements
Should not have
• bold or distracting colors or patterns

```html
<!DOCTYPE html>
<html lang="en">
<head>
<meta charset="utf-8">
<title>Newborn Adoption Process – Course Template</title>
<link href="https://fonts.googleapis.com/css2?family=Source+Sans+3:ital,wght@0,300;0,400;0,600;0,700;0,900;1,300;1,400&display=swap" rel="stylesheet">
<style>
:root{
  --orange:#e8722f;
  --orange-soft:#f2a57a;
  --ink:#2f2f2f;
  --text:#8a8a8a;
  --panel:#f1f1f1;
  --panel-2:#f7f7f7;
  --white:#ffffff;
  --brown:#7a3a12;
  --olive:#8a6d0b;
  --gold:#d9a400;
  --dark:#3b3431;
}
*{box-sizing:border-box;margin:0;padding:0}
html,body{width:1200px;height:2194px;overflow:hidden;background:var(--white)}
body{position:relative;font-family:"Source Sans 3",sans-serif;color:var(--ink)}
.slide{position:absolute;width:421px;height:236px;overflow:hidden;background:var(--panel);box-shadow:0 8px 22px rgba(0,0,0,.22)}
.col-l{left:113px}.col-r{left:666px}
.r1{top:54px}.r2{top:318px}.r3{top:581px}.r4{top:845px}.r5{top:1108px}.r6{top:1372px}.r7{top:1635px}.r8{top:1899px}
.abs{position:absolute}
.photo{position:absolute}
.title{font-weight:900;text-transform:uppercase;color:var(--ink);line-height:1.05;letter-spacing:.3px}
.sub{font-style:italic;font-weight:300;color:#666;font-size:10.5px}
.rule{display:block;width:22px;height:1px;background:#999;margin-top:6px}
.body{font-size:4.6px;line-height:2.35;color:var(--text);text-align:justify;font-weight:400}
.num{position:absolute;font-size:4.5px;color:#aaa;font-weight:600;letter-spacing:.3px}
.num b{color:var(--orange)}
.side{position:absolute;left:0;top:0;width:130px;height:100%;background:var(--panel-2)}
.stripe-l{position:absolute;left:0;top:0;width:6px;height:100%;background:var(--orange)}
.stripe-r{position:absolute;right:0;top:0;width:6px;height:100%;background:var(--orange)}
.frame{position:absolute;border:3px solid var(--orange)}
.white{background:var(--white)}
.card{position:absolute;top:72px;width:89px}
.card-head{background:var(--orange);color:#fff;font-weight:900;font-size:11px;text-align:center;padding:4px 0}
.card-body{background:rgba(50,42,38,.82);color:#ddd;font-size:4.6px;line-height:2.3;padding:6px 5px 4px;height:96px}
.card-bar{height:6px;border:1.5px solid var(--gold);margin:0 6px;position:relative;top:-10px}
.step{position:absolute;left:146px;width:258px;height:24px;border-bottom:1px solid #ddd;display:flex;align-items:center}
.step .lab{width:36px;font-size:6.5px;font-weight:900;padding-left:9px}
.step .txt{font-size:3.8px;line-height:1.6;color:var(--text);flex:1}
.tbl{position:absolute;left:148px;top:34px;width:258px;border-collapse:collapse;font-size:3.9px}
.tbl th{background:var(--orange);color:#fff;font-weight:700;height:16px}
.tbl td{height:17.3px;text-align:center;color:#555;border-bottom:1px solid #ddd}
.tbl td:first-child{text-align:left;font-weight:700;padding-left:3px;width:50px}
.tbl tr.total td{background:var(--dark);color:#fff;font-weight:700;border:none}
.dot{position:absolute;width:11px;height:11px;border-radius:50%;border:1.5px solid var(--orange);background:#fff}
.dot.ghost{border:1px dashed #bbb}
.month{position:absolute;font-size:4.5px;color:#888;transform:rotate(-70deg);transform-origin:left top}
.phase{position:absolute;font-size:4.4px;color:#888;line-height:1.6}
.phase b{display:block;color:var(--ink);font-size:4.8px;font-weight:900}
.big-dot{position:absolute;width:50px;height:50px;border-radius:50%;background:var(--orange);border:3px solid #f6c3a5;color:#fff;text-align:center;font-weight:900;font-size:14px;line-height:1;padding-top:11px}
.big-dot small{display:block;font-size:5px;font-weight:400;margin-top:2px}
.g-date{position:absolute;top:63px;font-size:4.5px;color:#777}
.g-bar{position:absolute;height:7px;background:repeating-linear-gradient(135deg,var(--orange) 0 3px,var(--orange-soft) 3px 5px);font-size:3.8px;color:#fff;padding-left:3px;line-height:7px}
.social{position:absolute;left:125px;width:10px;height:10px;background:var(--orange)}
</style>
</head>
<body>

<!-- 1 Cover -->
<section class="slide col-l r1">
  <div class="photo" style="left:0;top:0;width:270px;height:236px;background:linear-gradient(135deg,#5a4238,#9b7a6a 55%,#3d2f2a)" role="img" aria-label="Parent cradling a sleeping newborn"></div>
  <div class="abs" style="left:270px;top:0;width:4px;height:236px;background:var(--orange)"></div>
  <div class="photo" style="left:274px;top:0;width:147px;height:236px;background:linear-gradient(160deg,#f2e7e1,#f7f2ef)" role="img" aria-label="Faded close-up of a baby"></div>
  <div class="title abs" style="left:280px;top:70px;font-size:22px">Newborn<br>Adoption<br>Process.</div>
  <div class="abs" style="left:280px;top:178px;font-size:10px;font-weight:300;color:#555">Online course.</div>
  <div class="abs" style="left:280px;top:220px;font-size:5.5px;color:#666">City Name , April 4 2024</div>
</section>

<!-- 2 Introduction -->
<section class="slide col-r r1" style="background:var(--panel-2)">
  <p class="body abs" style="left:10px;top:16px;width:133px">Typesetting industry. Lorem ipsum has been the industry's standard dummy text ever since the 1500s, when an unknown printer took a galley of type and scrambled it to make a type specimen book. It has survived not only five centuries, but also the leap into electronic typesetting, remaining essentially unchanged. It was popularised in the 1960s with the release of transfer sheets containing lorem ipsum passages, and more recently with desktop publishing software including versions of lorem ipsum.</p>
  <div class="frame" style="left:185px;top:14px;width:227px;height:150px"></div>
  <div class="photo" style="left:191px;top:20px;width:215px;height:138px;background:linear-gradient(120deg,#e9e6e1,#d8c8b6 60%,#9a6a42)" role="img" aria-label="Sleeping baby in a knit hat beside a teddy bear"></div>
  <div class="title abs" style="left:184px;top:174px;font-size:23px">Introduction</div>
  <div class="abs" style="left:184px;top:203px;font-size:10px;font-weight:300;color:#555">Course Overview</div>
  <div class="num" style="left:10px;top:222px">SLIDE / <b>2</b></div>
</section>

<!-- 3 Information -->
<section class="slide col-l r2" style="background:var(--panel-2)">
  <div class="photo" style="left:0;top:0;width:165px;height:236px;background:linear-gradient(150deg,#cfc3b7,#a08472 55%,#7a604f)" role="img" aria-label="Smiling couple holding their baby"></div>
  <div class="frame" style="left:12px;top:35px;width:256px;height:158px"></div>
  <div class="title abs" style="left:82px;top:136px;font-size:22px">Information</div>
  <div class="abs" style="left:188px;top:168px;font-size:9.5px;font-weight:300;color:#555"><span style="display:inline-block;width:16px;height:1px;background:#777;vertical-align:middle;margin-right:3px"></span>Overwiev</div>
  <p class="body abs" style="left:282px;top:34px;width:124px">Typesetting industry. Lorem ipsum has been the industry's standard dummy text ever since the 1500s, when an unknown printer took a galley of type and scrambled it to make a type specimen book. It has survived not only five centuries, but also the leap into electronic typesetting, remaining essentially unchanged. It was popularized in the 1960s with the release of transfer sheets containing lorem ipsum passages, and more recently with desktop publishing software including versions of lorem ipsum</p>
  <div class="num" style="left:377px;top:222px">SLIDE / <b>3</b></div>
</section>

<!-- 4 Laughter -->
<section class="slide col-r r2">
  <div class="side white"></div><div class="stripe-l" style="width:4px"></div>
  <div class="title abs" style="left:14px;top:11px;font-size:14px">Laughter</div>
  <div class="sub abs" style="left:14px;top:29px">Subtitle slide here</div>
  <p class="body abs" style="left:14px;top:50px;width:108px">Lorem ipsum is simply dummy text of the printing and typesetting industry. Lorem ipsum has been the industry's standard dummy text ever since the 1500s, when an unknown printer took a galley of type and scrambled it to make a type specimen book. It has survived not only five centuries, but also the leap into electronic typesetting, remaining essentially unchanged. It was popularized in the 1960s with the release of transfer sheets containing lorem ipsum passages, and more recently with desktop publishing software including versions of lorem ipsum</p>
  <div class="num" style="left:14px;top:222px">SLIDE / <b>4</b></div>
  <svg class="abs" style="left:170px;top:8px" width="210" height="220" viewBox="0 0 210 220">
    <g fill="none" stroke-width="9">
      <path d="M18 96 A88 88 0 0 1 100 14" stroke="#8d8d8d"/>
      <path d="M110 14 A88 88 0 0 1 192 96" stroke="var(--gold)"/>
      <path d="M192 110 A88 88 0 0 1 110 192" stroke="var(--orange)"/>
      <path d="M100 192 A88 88 0 0 1 18 110" stroke="var(--brown)"/>
    </g>
    <path d="M100 6 L112 14 L100 22Z" fill="#8d8d8d"/>
    <path d="M184 96 L192 108 L200 96Z" fill="var(--gold)"/>
    <path d="M110 184 L98 192 L110 200Z" fill="var(--orange)"/>
    <path d="M10 110 L18 98 L26 110Z" fill="var(--brown)"/>
    <path d="M101 101 L101 28 A73 73 0 0 0 28 101Z" fill="#8d8d8d"/>
    <path d="M109 101 L109 28 A73 73 0 0 1 182 101Z" fill="var(--orange)"/>
    <path d="M101 109 L28 109 A73 73 0 0 0 101 182Z" fill="var(--brown)"/>
    <path d="M109 109 L182 109 A73 73 0 0 1 109 182Z" fill="var(--olive)"/>
    <g font-family="Source Sans 3,sans-serif" font-size="4" fill="#fff">
      <text x="50" y="55" font-weight="700">01 Lorem Ipsum</text>
      <text x="50" y="63">Short dummy text of the</text><text x="50" y="69">printing and typesetting</text><text x="50" y="75">industry since 1500s.</text>
      <text x="125" y="55" font-weight="700">02 Lorem Ipsum</text>
      <text x="125" y="63">Short dummy text of the</text><text x="125" y="69">printing and typesetting</text><text x="125" y="75">industry since 1500s.</text>
      <text x="50" y="125" font-weight="700">03 Lorem Ipsum</text>
      <text x="50" y="133">Short dummy text of the</text><text x="50" y="139">printing and typesetting</text><text x="50" y="145">industry since 1500s.</text>
      <text x="125" y="125" font-weight="700">04 Lorem Ipsum</text>
      <text x="125" y="133">Short dummy text of the</text><text x="125" y="139">printing and typesetting</text><text x="125" y="145">industry since 1500s.</text>
    </g>
  </svg>
  <div class="frame" style="left:372px;top:190px;width:38px;height:38px"></div>
</section>

<!-- 5 You decide -->
<section class="slide col-l r3">
  <div class="photo" style="left:0;top:0;width:421px;height:236px;background:linear-gradient(100deg,#d7b7a4 0%,#e2d6cc 45%,#8a776c 70%,#ddd6d1)" role="img" aria-label="Couple holding a newborn against a light wall"></div>
  <div class="abs" style="left:0;top:0;width:165px;height:236px;background:rgba(214,178,156,.75)"></div>
  <div class="frame" style="left:12px;top:16px;width:185px;height:205px"></div>
  <div class="title abs" style="left:24px;top:36px;font-size:14px">You decide</div>
  <p class="body abs" style="left:24px;top:60px;width:128px;color:#5a4a42;text-align:left">Lorem ipsum is simply dummy text of the printing and typesetting industry. Lorem ipsum has been the industry's standard dummy text ever since the 1500s, when an unknown printer took a galley of type and scrambled it to make a type specimen book. It has survived not only five centuries, but also the leap into electronic typesetting, remaining essentially unchanged. It was popularized in the 1960s with the release of transfer sheets containing lorem ipsum passages, and more recently with desktop publishing software including versions of lorem ipsum</p>
  <svg class="abs" style="left:240px;top:60px" width="120" height="120" viewBox="0 0 120 120">
    <circle cx="60" cy="60" r="42" fill="none" stroke="#fff" stroke-width="1" opacity=".8"/>
    <text x="48" y="82" font-family="Source Sans 3,sans-serif" font-size="62" font-weight="900" fill="#fff" opacity=".55">1</text>
    <circle cx="33" cy="28" r="11" fill="var(--orange)"/>
    <circle cx="22" cy="60" r="5" fill="var(--orange)"/>
    <circle cx="42" cy="101" r="11" fill="var(--orange)"/>
    <circle cx="100" cy="90" r="8" fill="var(--orange)"/>
    <circle cx="95" cy="28" r="5" fill="var(--orange)"/>
    <path d="M100 94 l-3.5 -3.5 a2 2 0 0 1 3.5 -2.5 a2 2 0 0 1 3.5 2.5z" fill="#fff"/>
  </svg>
</section>

<!-- 6 You decide – four columns -->
<section class="slide col-r r3">
  <div class="photo" style="left:0;top:0;width:421px;height:236px;background:linear-gradient(100deg,#4a3a32,#a88a6a 40%,#6a5244 70%,#c6a07a)" role="img" aria-label="Family outdoors in warm light"></div>
  <div class="abs" style="left:0;top:0;width:421px;height:236px;background:rgba(40,32,28,.45)"></div>
  <div class="title abs" style="left:10px;top:11px;font-size:14px;color:#fff">You decide</div>
  <div class="sub abs" style="left:10px;top:29px;color:#eee">Subtitle slide here</div>
  <div class="card" style="left:22px"><div class="card-head">SUBTITLED</div><div class="card-body">Lorem ipsum dolor sit amet, consectetur adipiscing elit. Morbi libero sapien, cursus eget lorem at, convallis hendrerit tortor. Duis vulputate pellentesque dui eget ornare. Aliquam dignissim placerat auctor.</div><div class="card-bar"></div></div>
  <div class="card" style="left:118px"><div class="card-head">SUBTITLED</div><div class="card-body">Lorem ipsum dolor sit amet, consectetur adipiscing elit. Morbi libero sapien, cursus eget lorem at, convallis hendrerit tortor. Duis vulputate pellentesque dui eget ornare. Aliquam dignissim placerat auctor.</div><div class="card-bar"></div></div>
  <div class="card" style="left:213px"><div class="card-head">SUBTITLED</div><div class="card-body">Lorem ipsum dolor sit amet, consectetur adipiscing elit. Morbi libero sapien, cursus eget lorem at, convallis hendrerit tortor. Duis vulputate pellentesque dui eget ornare. Aliquam dignissim placerat auctor.</div><div class="card-bar"></div></div>
  <div class="card" style="left:309px"><div class="card-head">SUBTITLED</div><div class="card-body">Lorem ipsum dolor sit amet, consectetur adipiscing elit. Morbi libero sapien, cursus eget lorem at, convallis hendrerit tortor. Duis vulputate pellentesque dui eget ornare. Aliquam dignissim placerat auctor.</div><div class="card-bar"></div></div>
</section>

<!-- 7 Difference – steps -->
<section class="slide col-l r4 white">
  <div class="side"></div><div class="stripe-l"></div>
  <div class="abs" style="left:15px;top:85px"><div class="title" style="font-size:14px">What's the<br>difference?</div><div class="sub" style="margin-top:2px">Subtitle slide here</div><span class="rule"></span></div>
  <div class="num" style="left:10px;top:222px">SLIDE / <b>7</b></div>
  <div class="abs" style="left:146px;top:43px;width:2px;height:144px;background:linear-gradient(var(--ink),var(--orange) 30%,#e0b090 50%,var(--orange) 70%,var(--brown))"></div>
  <div class="step" style="top:43px"><span class="lab">STEP</span><span class="txt">Duis vulputate pellentesque dui eget ornare. Aliquam dignissim placerat auctor. Lorem ipsum dolor sit amet, consectetur adipiscing elit. Morbi libero sapien, cursus eget lorem at, convallis hendrerit tortor.</span></div>
  <div class="step" style="top:67px"><span class="lab">STEP</span><span class="txt">Duis vulputate pellentesque dui eget ornare. Aliquam dignissim placerat auctor. Lorem ipsum dolor sit amet, consectetur adipiscing elit. Morbi libero sapien, cursus eget lorem at, convallis hendrerit tortor.</span></div>
  <div class="step" style="top:91px"><span class="lab">STEP</span><span class="txt">Duis vulputate pellentesque dui eget ornare. Aliquam dignissim placerat auctor. Lorem ipsum dolor sit amet, consectetur adipiscing elit. Morbi libero sapien, cursus eget lorem at, convallis hendrerit tortor.</span></div>
  <div class="step" style="top:115px"><span class="lab">STEP</span><span class="txt">Duis vulputate pellentesque dui eget ornare. Aliquam dignissim placerat auctor. Lorem ipsum dolor sit amet, consectetur adipiscing elit. Morbi libero sapien, cursus eget lorem at, convallis hendrerit tortor.</span></div>
  <div class="step" style="top:139px"><span class="lab">STEP</span><span class="txt">Duis vulputate pellentesque dui eget ornare. Aliquam dignissim placerat auctor. Lorem ipsum dolor sit amet, consectetur adipiscing elit. Morbi libero sapien, cursus eget lorem at, convallis hendrerit tortor.</span></div>
  <div class="step" style="top:163px"><span class="lab">STEP</span><span class="txt">Duis vulputate pellentesque dui eget ornare. Aliquam dignissim placerat auctor. Lorem ipsum dolor sit amet, consectetur adipiscing elit. Morbi libero sapien, cursus eget lorem at, convallis hendrerit tortor.</span></div>
</section>

<!-- 8 Difference – text -->
<section class="slide col-r r4 white">
  <div class="side"></div><div class="stripe-l"></div>
  <div class="abs" style="left:15px;top:85px"><div class="title" style="font-size:14px">What's the<br>difference?</div><div class="sub" style="margin-top:2px">Subtitle slide here</div><span class="rule"></span></div>
  <div class="num" style="left:10px;top:222px">SLIDE / <b>8</b></div>
  <p class="body abs" style="left:160px;top:40px;width:226px">Typesetting industry. Lorem ipsum has been the industry's standard dummy text ever since the 1500s, when an unknown printer took a galley of type and scrambled it to make a type specimen book. It has survived not only five centuries, but also the leap into electronic typesetting, remaining essentially unchanged. It was popularized in the 1960s with the release of transfer sheets containing.</p>
  <p class="body abs" style="left:160px;top:128px;width:226px">Typesetting industry. Lorem ipsum has been the industry's standard dummy text ever since the 1500s, when an unknown printer took a galley of type and scrambled it to make a type specimen book. It has survived not only five centuries, but also the leap into electronic typesetting, remaining essentially unchanged. It was popularized in the 1960s with the release of transfer sheets containing.</p>
</section>

<!-- 9 Money as a right -->
<section class="slide col-l r5 white">
  <div class="abs" style="left:256px;top:0;width:165px;height:236px;background:var(--panel-2)"></div><div class="stripe-r"></div>
  <ul class="body abs" style="left:24px;top:40px;width:216px;list-style:disc">
    <li>Typesetting industry. Lorem ipsum has been the industry's standard dummy text ever since the 1500s, when an unknown printer took a galley of type</li>
    <li>And scrambled it to make a type specimen book. It has survived not only five centuries, but also the leap into electronic typesetting, remaining essentially unchanged. It was popularized in the 1960s with the release of transfer sheets containing.</li>
    <li>Typesetting industry. Lorem ipsum has been the industry's standard dummy text ever since the 1500s, when an unknown printer took a galley of type</li>
    <li>And scrambled it to make a type specimen book. It has survived not only five centuries, but also the leap into electronic typesetting, remaining essentially unchanged. It was popularized in the 1960s with the release of transfer sheets containing.</li>
  </ul>
  <div class="abs" style="left:286px;top:92px"><div class="title" style="font-size:14px">Money as<br>&nbsp;a “right.”</div><div class="sub" style="margin-top:2px">Subtitle slide here</div><span class="rule"></span></div>
  <div class="num" style="left:371px;top:222px">SLIDE / <b>9</b></div>
</section>

<!-- 10 Here's how -->
<section class="slide col-r r5 white">
  <div class="side"></div><div class="stripe-l"></div>
  <div class="abs" style="left:15px;top:100px"><div class="title" style="font-size:14px">Here's how:</div><div class="sub" style="margin-top:2px">Subtitle slide here</div><span class="rule"></span></div>
  <div class="num" style="left:10px;top:222px">SLIDE / <b>10</b></div>
  <p class="body abs" style="left:180px;top:40px;width:206px">Typesetting industry. Lorem ipsum has been the industry's standard dummy text ever since the 1500s, when an unknown printer took a galley of type and scrambled it to make a type specimen book. It has survived not only five centuries, but also the leap into electronic typesetting, remaining essentially unchanged. It was popularized in the 1960s with the release of transfer sheets containing.</p>
  <p class="body abs" style="left:180px;top:128px;width:206px">Typesetting industry. Lorem ipsum has been the industry's standard dummy text ever since the 1500s, when an unknown printer took a galley of type and scrambled it to make a type specimen book. It has survived not only five centuries, but also the leap into electronic typesetting, remaining essentially unchanged. It was popularized in the 1960s with the release of transfer sheets containing.</p>
</section>

<!-- 11 Section divider -->
<section class="slide col-l r6">
  <div class="photo" style="left:0;top:0;width:421px;height:236px;background:linear-gradient(110deg,#c7a690,#e9c2a4 40%,#d99a72 70%,#edd6c6)" role="img" aria-label="Parents playing with their baby on a bed"></div>
  <div class="abs" style="left:10px;top:10px;width:411px;height:216px;background:rgba(232,114,47,.38)"></div>
  <div class="title abs" style="left:75px;top:168px;font-size:29px;color:#fff">Section slide</div>
  <div class="abs" style="left:275px;top:200px;font-size:9px;color:#fff;font-weight:300">Divider</div>
  <div class="frame" style="left:325px;top:141px;width:90px;height:95px"></div>
  <div class="abs" style="left:338px;top:160px;font-size:46px;font-weight:400;color:#fff;line-height:1">01</div>
</section>

<!-- 12 Perception chart -->
<section class="slide col-r r6 white">
  <div class="side" style="background:var(--panel)"></div><div class="stripe-l" style="width:4px"></div>
  <div class="title abs" style="left:14px;top:10px;font-size:14px">Perception<br>chart</div>
  <div class="sub abs" style="left:14px;top:47px">Subtitle slide here</div>
  <p class="body abs" style="left:14px;top:68px;width:110px">Typesetting industry. Lorem ipsum has been the industry's standard dummy text ever since the 1500s, when an unknown printer took a galley of type and scrambled it to make a type specimen book. It has survived not only five centuries, but also the leap into electronic typesetting, remaining essentially unchanged. It was popularized in the 1960s with the release of transfer sheets containing.</p>
  <div class="num" style="left:10px;top:222px">SLIDE / <b>12</b></div>
  <table class="tbl">
    <tr><th></th><th>COLUMN 1</th><th>COLUMN 2</th><th>COLUMN 3</th><th>COLUMN 4</th></tr>
    <tr><td>Row Sample 01</td><td>329</td><td>368</td><td>388</td><td>408</td></tr>
    <tr><td>Row Sample 02</td><td>295</td><td>325</td><td>345</td><td>365</td></tr>
    <tr><td>Row Sample 03</td><td>256</td><td>296</td><td>316</td><td>336</td></tr>
    <tr><td>Row Sample 04</td><td>123</td><td>163</td><td>183</td><td>203</td></tr>
    <tr><td>Row Sample 05</td><td>532</td><td>572</td><td>592</td><td>612</td></tr>
    <tr><td>Row Sample 06</td><td>256</td><td>296</td><td>316</td><td>336</td></tr>
    <tr><td>Row Sample 07</td><td>985</td><td>1025</td><td>1045</td><td>1065</td></tr>
    <tr><td>Row Sample 08</td><td>645</td><td>685</td><td>705</td><td>725</td></tr>
    <tr><td>Row Sample 09</td><td>766</td><td>806</td><td>826</td><td>846</td></tr>
    <tr class="total"><td>Total Row</td><td>4176</td><td>4356</td><td>4536</td><td>4716</td></tr>
  </table>
</section>

<!-- 13 Process timeline start -->
<section class="slide col-l r7 white">
  <div class="side"></div><div class="stripe-l"></div>
  <div class="title abs" style="left:15px;top:60px;font-size:14px">Newborn<br>adoption<br>process</div>
  <div class="sub abs" style="left:15px;top:116px">Subtitle slide here</div>
  <p class="body abs" style="left:15px;top:136px;width:110px;text-align:left">Lorem ipsum dolor sit amet, consectetur adipiscing elit. Morbi libero sapien, cursus eget lorem at, convallis hendrerit tortor. Duis vulputate pellentesque dui eget ornare. Aliquam dignissim placerat auctor.</p>
  <div class="num" style="left:10px;top:222px">SLIDE / <b>13</b></div>
  <div class="abs" style="left:140px;top:122px;width:281px;height:1px;background:#ccc"></div>
  <svg class="abs" style="left:130px;top:40px" width="291" height="160" viewBox="0 0 291 160" fill="none" stroke="#bbb" stroke-width=".7">
    <path d="M8 12 H28 L82 76"/><path d="M160 12 H178 L235 76"/><path d="M90 146 H105 L158 90"/>
  </svg>
  <div class="big-dot" style="left:141px;top:97px">start<small>2024</small></div>
  <div class="dot" style="left:207px;top:117px"></div><div class="dot ghost" style="left:245px;top:117px"></div>
  <div class="dot" style="left:283px;top:117px"></div><div class="dot ghost" style="left:321px;top:117px"></div>
  <div class="dot" style="left:360px;top:117px"></div><div class="dot ghost" style="left:398px;top:117px"></div>
  <span class="month" style="left:205px;top:150px">January</span><span class="month" style="left:243px;top:150px">February</span>
  <span class="month" style="left:283px;top:146px">March</span><span class="month" style="left:320px;top:146px">April</span>
  <span class="month" style="left:360px;top:143px">May</span><span class="month" style="left:398px;top:143px">June</span>
  <div class="phase" style="left:138px;top:46px"><b>PHASE 01</b>Morbi libero sapien, cursus<br>eget lorem at, convallis<br>hendrerit tortor</div>
  <div class="phase" style="left:290px;top:46px"><b>PHASE 03</b>Morbi libero sapien, cursus<br>eget lorem at, convallis<br>hendrerit tortor</div>
  <div class="phase" style="left:214px;top:180px"><b>PHASE 02</b>Morbi libero sapien, cursus<br>eget lorem at, convallis<br>hendrerit tortor</div>
</section>

<!-- 14 Process timeline end -->
<section class="slide col-r r7 white">
  <div class="abs" style="left:290px;top:0;width:131px;height:236px;background:var(--panel-2)"></div><div class="stripe-r"></div>
  <div class="abs" style="left:0;top:122px;width:120px;height:1px;background:#ccc"></div>
  <div class="abs" style="left:132px;top:55px;width:77px;height:140px;border-left:1px dashed #aaa;border-right:1px dashed #aaa"></div>
  <div class="abs" style="left:140px;top:122px;width:62px;border-top:1.5px dashed var(--orange)"></div>
  <div class="abs" style="left:209px;top:122px;width:30px;height:1px;background:#ccc"></div>
  <div class="abs" style="left:145px;top:58px;width:52px;text-align:center;font-size:5.5px;font-weight:900;line-height:1.2">ADOPTION<br>WAITING TIME</div>
  <div class="abs" style="left:38px;top:75px;width:36px;text-align:center;font-size:4.8px;font-weight:900;line-height:1.2">SUMMARY<br>MEETING</div>
  <div class="abs" style="left:56px;top:83px;width:1px;height:34px;background:#bbb"></div>
  <div class="dot ghost" style="left:11px;top:117px"></div>
  <div class="dot" style="left:51px;top:117px;background:var(--orange);border-color:#b04f18"></div>
  <div class="dot ghost" style="left:89px;top:117px"></div>
  <span class="month" style="left:16px;top:146px">July</span><span class="month" style="left:54px;top:150px;color:#444">August</span><span class="month" style="left:92px;top:158px">September</span>
  <div class="big-dot" style="left:229px;top:97px">End<small>2016</small></div>
  <p class="body abs" style="left:300px;top:92px;width:110px;text-align:left">Lorem ipsum dolor sit amet, consectetur adipiscing elit. Morbi libero sapien, cursus eget lorem at, convallis hendrerit tortor. Duis vulputate pellentesque dui eget ornare. Aliquam dignissim placerat auctor.</p>
  <div class="num" style="left:378px;top:222px">SLIDE / <b>14</b></div>
</section>

<!-- 15 Gantt chart -->
<section class="slide col-l r8">
  <div class="photo" style="left:155px;top:0;width:266px;height:236px;background:linear-gradient(120deg,#e7e0da,#c9b8ab 50%,#ece6e1)" role="img" aria-label="Faded photo of a parent smiling at a baby"></div>
  <div class="abs" style="left:0;top:0;width:155px;height:236px;background:var(--orange-soft)"></div>
  <div class="title abs" style="left:18px;top:46px;font-size:14px">Process gant<br>chart</div>
  <p class="abs" style="left:18px;top:91px;width:128px;font-size:7px;line-height:2.2;color:#6a3a20">Duis vulputate pellentesque dui eget ornare. Aliquam dignissim placerat auctor. Lorem ipsum dolor sit amet, consectetur adipiscing elit. Morbi libero sapien, cursus eget lorem at, convallis hendrerit tortor.</p>
  <span class="g-date" style="left:175px">&lt;date&gt;</span><span class="g-date" style="left:212px">&lt;date&gt;</span><span class="g-date" style="left:249px">&lt;date&gt;</span>
  <span class="g-date" style="left:303px">&lt;date&gt;</span><span class="g-date" style="left:340px">&lt;date&gt;</span><span class="g-date" style="left:377px">&lt;date&gt;</span>
  <div class="g-bar" style="left:165px;top:108px;width:90px">Start</div>
  <div class="g-bar" style="left:200px;top:135px;width:95px">Phase 2</div>
  <div class="g-bar" style="left:280px;top:162px;width:90px">Phase 3</div>
  <div class="g-bar" style="left:370px;top:189px;width:38px">Implementation</div>
</section>

<!-- 16 Thank you -->
<section class="slide col-r r8">
  <div class="photo" style="left:0;top:0;width:421px;height:236px;background:linear-gradient(100deg,#dcdde0,#b8b6b7 45%,#6a5a52 65%,#d2d3d6)" role="img" aria-label="Couple holding a newborn against a grey wall"></div>
  <div class="abs" style="left:13px;top:61px;width:130px;height:136px;background:rgba(236,236,238,.85)"></div>
  <div class="frame" style="left:10px;top:58px;width:138px;height:142px"></div>
  <div class="title abs" style="left:22px;top:92px;font-size:14px">Thank you</div>
  <div class="abs" style="left:22px;top:110px;font-size:6.5px;font-weight:900">CONTACT</div>
  <div class="abs" style="left:22px;top:119px;font-size:5.2px;line-height:1.45;color:#555">Harbor Adoption Team<br>555 010 2040<br>hello@harboradoption.org<br>Company adress<br>214 Maple Lane<br>00000 Fairview, US</div>
  <div class="social" style="top:104px"></div>
  <div class="social" style="top:119px"></div>
  <div class="social" style="top:134px"></div>
</section>

</body>
</html>
```